Fair Wind golf balls - the Lantern Collection

I need to design a box for 12 golf balls.
It is the actual lid and sides that need the creative.
Attached is layout that doesn't pop enough.
Someone needs to make it look more prominent
when displayed on Vendora, etc.
I launched the Song of the Heron golf balls - the Meadow Collection
back in 2010. It turned into a flash fad.
That is my goal here .

Please see attached file. My son says it needs to be more
modern, and compared to the golf balls on Vendora looks far
too dull.
Updates

Reason: My initial 5 day window wasn't enough time. Rookies make mistakes. Thanks Owen

Target Market(s)

Women golfers in US and UK

Requirements
Must have
• Classy

```html
<!DOCTYPE html>
<html lang="en">
<head>
<meta charset="utf-8">
<title>Fair Wind Golf Balls – Box Dieline</title>
<link rel="stylesheet" href="https://fonts.googleapis.com/css2?family=Courgette&family=Roboto+Condensed:wght@400&display=swap">
<style>
  :root{
    --sky:#3ea4dd;
    --sky-pale:#d9eefa;
    --white:#ffffff;
    --green:#8fd14f;
    --green-light:#c9ec8f;
    --green-deep:#5fb22e;
    --ink:#262626;
    --ball:#e9ecef;
    --ball-shade:#b9bfc6;
    --fold:#2a86c2;
  }
  *{margin:0;padding:0;box-sizing:border-box}
  html,body{width:1200px;height:790px;overflow:hidden;background:var(--white)}
  .dieline{position:relative;width:1200px;height:790px;overflow:hidden;background:var(--white)}

  .panel{position:absolute;overflow:hidden}
  .lid{left:293px;top:160px;width:614px;height:468px;
    background:radial-gradient(ellipse 60% 55% at 45% 55%,var(--white) 0%,var(--sky-pale) 55%,var(--sky) 100%)}
  .flap{left:293px;width:614px;background:linear-gradient(180deg,var(--sky) 0%,#8fc9ee 60%,var(--sky) 100%)}
  .flap--bottom{top:628px;height:162px}
  .flap--top{top:0;height:160px;transform:rotate(180deg)}
  .side{top:160px;height:468px;
    background:linear-gradient(180deg,var(--sky) 0%,var(--sky) 12%,var(--white) 48%,var(--white) 52%,var(--sky) 88%,var(--sky) 100%)}
  .side--left{left:0;width:293px}
  .side--right{left:907px;width:293px}
  .fold-line{position:absolute;top:0;width:1px;height:100%;background:var(--fold);opacity:.6}

  .waves{position:absolute;inset:0;width:100%;height:100%}

  .photo{position:absolute;border-radius:50%;border:4px solid var(--white);
    background:linear-gradient(180deg,#a9cbee 0%,#dfeaf5 55%,#6da542 70%,#4f8a2c 100%)}
  .ball{position:absolute;border-radius:50%;
    background:radial-gradient(circle at 38% 35%,var(--white) 0%,var(--ball) 45%,var(--ball-shade) 100%)}
  .turf{position:absolute;border-radius:50% 50% 0 0;
    background:linear-gradient(180deg,var(--green-light),var(--green-deep))}

  .script{font-family:"Courgette",cursive;color:var(--ink);white-space:nowrap}
  .sans{font-family:"Roboto Condensed",sans-serif;color:var(--ink);white-space:nowrap}

  .collection{position:absolute;left:47px;top:96px;font-size:21px}
  .brand-main{position:absolute;left:232px;top:200px;font-size:62px;line-height:1}
  .tag-main{position:absolute;left:385px;top:286px;font-size:20px;line-height:1}
  .quote{position:absolute;left:102px;top:400px;font-size:21px;color:var(--white);
    transform:rotate(-7deg);transform-origin:left center}

  .brand-flap{position:absolute;left:205px;top:46px;font-size:40px;line-height:1}
  .tag-flap{position:absolute;left:299px;top:100px;font-size:13px;line-height:1}

  .side-copy{position:absolute;writing-mode:vertical-rl;height:290px;display:flex;flex-direction:column}
  .side-copy .line{font-size:19px;width:32px;line-height:32px}
  .side-copy .brand-side{font-size:26px;width:36px;line-height:36px}
  .side-copy .small{font-size:11px;width:26px;line-height:26px}
  .side--left .side-copy{left:174px;top:95px}
  .side--left .side-copy .small{padding-top:48px}
  .side--right .side-copy{left:22px;top:88px;transform:rotate(180deg)}
  .side--right .side-copy .small{padding-top:82px}
</style>
</head>
<body>
<div class="dieline">

  <section class="panel flap flap--top">
    <svg class="waves" viewBox="0 0 614 160" preserveAspectRatio="none" aria-hidden="true">
      <path d="M0 30 C150 70 300 10 614 60 L614 0 L0 0Z" fill="var(--green-light)" opacity=".7"/>
      <path d="M0 110 C200 60 420 150 614 100 L614 160 L0 160Z" fill="var(--green)" opacity=".5"/>
    </svg>
    <div class="turf" style="left:140px;top:90px;width:180px;height:70px" role="img" aria-label="Green grass tuft"></div>
    <div class="ball" style="left:42px;top:7px;width:112px;height:112px" role="img" aria-label="White golf ball"></div>
    <span class="script brand-flap">Fair Wind</span>
    <span class="sans tag-flap">GOLF BALLS</span>
    <div class="photo" style="left:455px;top:5px;width:140px;height:140px" role="img" aria-label="Photo of a woman golfer addressing the ball on a tee"></div>
  </section>

  <section class="panel side side--left">
    <span class="fold-line" style="left:147px"></span>
    <div class="side-copy">
      <span class="sans line">In a head-to-head competition...</span>
      <span class="script brand-side">Fair Wind Golf Balls</span>
      <span class="sans small">Made in United State of America</span>
    </div>
  </section>

  <section class="panel lid">
    <svg class="waves" viewBox="0 0 614 468" preserveAspectRatio="none" aria-hidden="true">
      <path d="M0 0 L614 0 L614 20 C450 10 300 70 0 40Z" fill="var(--green)"/>
      <path d="M0 40 C250 75 420 20 614 40 L614 55 C420 40 250 100 0 70Z" fill="var(--green-light)"/>
      <path d="M0 80 C200 110 400 60 614 90" stroke="var(--green)" stroke-width="3" fill="none" opacity=".8"/>
      <path d="M0 360 C200 330 420 300 614 340 L614 468 L0 468Z" fill="var(--green-light)"/>
      <path d="M0 410 C220 400 420 330 614 360 L614 468 L0 468Z" fill="var(--green)"/>
      <path d="M0 440 C250 430 420 380 614 400" stroke="var(--white)" stroke-width="2" fill="none" opacity=".8"/>
      <path d="M0 455 C250 450 420 410 614 430" stroke="var(--sky)" stroke-width="3" fill="none" opacity=".7"/>
    </svg>
    <div class="turf" style="left:60px;top:320px;width:260px;height:90px" role="img" aria-label="Green grass tuft"></div>
    <span class="sans collection">The Lantern Collection</span>
    <div class="ball" style="left:64px;top:218px;width:144px;height:144px" role="img" aria-label="White golf ball"></div>
    <span class="script brand-main">Fair Wind</span>
    <span class="sans tag-main">GOLF BALLS</span>
    <div class="photo" style="left:419px;top:14px;width:180px;height:180px" role="img" aria-label="Photo of a woman golfer standing over a driver on the tee"></div>
    <span class="script quote">“Hell hath no fury like a woman scorned”</span>
  </section>

  <section class="panel side side--right">
    <span class="fold-line" style="left:146px"></span>
    <div class="side-copy">
      <span class="sans line">...the little head sometimes wins.</span>
      <span class="script brand-side">Fair Wind Golf Balls</span>
      <span class="sans small">fairwindgolfball.com</span>
    </div>
  </section>

  <section class="panel flap flap--bottom">
    <svg class="waves" viewBox="0 0 614 162" preserveAspectRatio="none" aria-hidden="true">
      <path d="M0 30 C150 70 300 10 614 60 L614 0 L0 0Z" fill="var(--green-light)" opacity=".7"/>
      <path d="M0 110 C200 60 420 150 614 100 L614 162 L0 162Z" fill="var(--green)" opacity=".5"/>
    </svg>
    <div class="turf" style="left:140px;top:90px;width:180px;height:72px" role="img" aria-label="Green grass tuft"></div>
    <div class="ball" style="left:42px;top:5px;width:114px;height:114px" role="img" aria-label="White golf ball"></div>
    <span class="script brand-flap">Fair Wind</span>
    <span class="sans tag-flap">GOLF BALLS</span>
    <div class="photo" style="left:455px;top:8px;width:144px;height:144px" role="img" aria-label="Photo of a woman golfer addressing the ball on a tee"></div>
  </section>

</div>
</body>
</html>
```